Letter Head

We need a letter head desgn (A4).
Header Marcus Fennell Creative
phone number 0438571604
email marcusfennellcreative@quillpost.net

Footer ABN 57 314 629 105

```html
<!DOCTYPE html>
<html lang="en">
<head>
<meta charset="utf-8">
<title>Marcus Fennell Creative – Letterhead</title>
<link href="https://fonts.googleapis.com/css2?family=Arimo:wght@400;700&display=swap" rel="stylesheet">
<style>
  :root {
    --page: #ffffff;
    --page-edge: #b5b5b5;
    --green-base: #3aa935;
    --green-lime: #a6cf3a;
    --green-pale: #c6e07a;
    --green-mid: #5cb848;
    --green-deep: #00923f;
    --green-teal: #2eaa5c;
    --ink-white: #ffffff;
    --footer-black: #1b1b1b;
    --footer-slate: #34344f;
    --footer-teal: #1c6a6c;
    --mark-tint: #d3e9d6;
  }
  * { margin: 0; padding: 0; box-sizing: border-box; }
  html, body { width: 900px; height: 1200px; overflow: hidden; background: var(--page); }
  .letterhead {
    position: relative;
    width: 900px;
    height: 1200px;
    background: var(--page);
    border: 1px solid var(--page-edge);
    font-family: "Arimo", Arial, sans-serif;
    color: var(--ink-white);
    overflow: hidden;
  }
  .header { position: absolute; top: 0; left: 0; width: 900px; height: 178px; }
  .header-shapes, .footer-shapes { position: absolute; inset: 0; width: 100%; height: 100%; }
  .brand {
    position: absolute;
    left: 56px;
    top: 34px;
    font-weight: 700;
    color: var(--ink-white);
    line-height: 1;
    white-space: nowrap;
  }
  .brand-name { font-size: 76px; letter-spacing: -1px; display: block; }
  .brand-sub { font-size: 24px; letter-spacing: 0.3px; display: block; margin-top: 2px; }
  .services {
    position: absolute;
    left: 497px;
    top: 44px;
    font-size: 14px;
    line-height: 14px;
    color: var(--ink-white);
    list-style: none;
    white-space: nowrap;
  }
  .contact {
    position: absolute;
    left: 637px;
    top: 44px;
    list-style: none;
    font-size: 14px;
    color: var(--ink-white);
    white-space: nowrap;
  }
  .contact li { display: flex; align-items: center; height: 27px; }
  .contact svg { width: 16px; height: 16px; margin-right: 4px; flex: none; }
  .camera-mark {
    position: absolute;
    left: 272px;
    top: 471px;
    width: 357px;
    height: 256px;
    background: linear-gradient(90deg, #f6fbf6 0%, var(--mark-tint) 60%);
  }
  .footer { position: absolute; left: 0; bottom: 0; width: 900px; height: 88px; background: var(--footer-black); }
  .abn {
    position: absolute;
    right: 26px;
    top: 32px;
    font-size: 22px;
    color: var(--ink-white);
  }
</style>
</head>
<body>
<div class="letterhead">
  <header class="header">
    <svg class="header-shapes" viewBox="0 0 900 178" preserveAspectRatio="none" aria-hidden="true">
      <defs>
        <linearGradient id="limeFade" x1="0" y1="0" x2="1" y2="0">
          <stop offset="0" stop-color="#c3e07d"/>
          <stop offset="1" stop-color="#5fb848"/>
        </linearGradient>
      </defs>
      <rect width="900" height="178" fill="var(--green-base)"/>
      <polygon points="0,0 155,0 0,178" fill="var(--green-lime)"/>
      <polygon points="155,0 0,178 600,178 380,30" fill="url(#limeFade)"/>
      <polygon points="160,0 900,0 900,155 420,40" fill="var(--green-teal)" opacity="0.7"/>
      <polygon points="600,178 900,60 900,178" fill="var(--green-deep)"/>
      <polygon points="760,0 900,0 900,60 830,40" fill="var(--green-deep)"/>
    </svg>

    <div class="brand">
      <span class="brand-name">MARCUS</span>
      <span class="brand-sub">FENNELL CREATIVE</span>
    </div>

    <ul class="services">
      <li>photography</li>
      <li>video</li>
      <li>design</li>
    </ul>

    <ul class="contact">
      <li>
        <svg viewBox="0 0 16 16" aria-hidden="true"><circle cx="8" cy="8" r="8" fill="#fff"/><path d="M5 4.5c.5-.5 1-.5 1.3 0l.8 1.3c.2.4 0 .8-.3 1l-.4.3c.4.9 1.1 1.6 2 2l.3-.4c.2-.3.6-.5 1-.3l1.3.8c.5.3.5.8 0 1.3-.8.8-2 .9-3.2.1A8 8 0 0 1 4.9 7.7C4.1 6.5 4.2 5.3 5 4.5z" fill="#3aa935"/></svg>
        0438 571 604
      </li>
      <li>
        <svg viewBox="0 0 16 16" aria-hidden="true"><circle cx="8" cy="8" r="8" fill="#fff"/><rect x="4" y="5" width="8" height="6" rx="1" fill="none" stroke="#3aa935" stroke-width="1.2"/><path d="M4.3 5.5 8 8.5l3.7-3" fill="none" stroke="#3aa935" stroke-width="1.2"/></svg>
        marcusfennellcreative@quillpost.net
      </li>
      <li>
        <svg viewBox="0 0 16 16" aria-hidden="true"><circle cx="8" cy="8" r="7" fill="none" stroke="#fff" stroke-width="1.3"/><ellipse cx="8" cy="8" rx="3" ry="7" fill="none" stroke="#fff" stroke-width="1.1"/><path d="M1 8h14M2.2 4.5h11.6M2.2 11.5h11.6" stroke="#fff" stroke-width="1.1"/></svg>
        www.fennellcreative.com.au
      </li>
    </ul>
  </header>

  <div class="camera-mark" role="img" aria-label="Faint pale green camera emblem placed as a watermark in the centre of the page"></div>

  <footer class="footer">
    <svg class="footer-shapes" viewBox="0 0 900 88" preserveAspectRatio="none" aria-hidden="true">
      <defs>
        <linearGradient id="footerFade" x1="0" y1="0" x2="1" y2="0">
          <stop offset="0" stop-color="var(--footer-slate)"/>
          <stop offset="1" stop-color="var(--footer-teal)"/>
        </linearGradient>
      </defs>
      <polygon points="330,0 900,0 900,88 240,88" fill="url(#footerFade)"/>
      <polygon points="330,0 410,0 240,88 200,88" fill="#262633"/>
      <polygon points="600,0 900,0 900,40" fill="#246467" opacity="0.6"/>
    </svg>
    <p class="abn">ABN 57 314 629 105</p>
  </footer>
</div>
</body>
</html>
```